Systems and Technology Consultants - Website

Design & Build a website for a new company which operates in the Systems and Technology space for Transportation, Government and Commercial sectors.

Overall design should be minimalist in nature.
Should also have a feed that provides news and event updates on the main page.
Logo has already been awarded and should be incorporated into the site.

We like the overall layout, functionality and simplicity of the below sites. Submitted designs could be similar to or a combination of the aspects on these sites, or perhaps a whole different concept - we are open to new ideas.
Vortrane.com
Merp.it

Update 1 Dated 27 May 2014

All I am moving away from the Merp.it website and would like it to be more aligned with Vortrane.com not only in layout but in functionality. I will be extending the deadline of this design brief for two weeks to incorporate additional requirements and will add addtional funding to the project.

Apologies for not having more information available to provide but with so many submissions its getting confusing.

Thanks Dermot
Updates

Please note that the brief has been updated and the deadline has been extended.

Important: We will need two language versions of the website, English and Arabic; the website is hosted on HostPeak

Hello All, Thank you for your submissions. We have narrowed it down to the final 6 designers and I just wanted to take a moment and provide a bit of feedback regarding the concepts that we like and the modifications we are looking for. First, let me mention some of the design functions we like. - At the top of the homepage we really like the "region" or "language" tab so that the website can be viewed in both English and Arabic. - We like the homepage to have clear color variation so that the different sections of the homepage are distinct. Additionally, we like the bottom portion of the homepage to be in red. We feel that draws attention to our contact information. Again, we would like the colors to integrate black, gray-scale, red, etc. - Having a search tab at the top of the home page, or integrated into the main image, so that the site is easy to navigate. - We especially like the main image to have the scrolling tabs at the bottom so it is easy to browse the services offered (Consultancy, Solutions Architecture, Masters Systems Integration, Independent Design Review). - In regards to the services offered tab we really like the idea that a few people presented that have the outside of our logo with an icon in the middle of consultancy, solutions, etc., etc. Secondly, as mentioned in our brief we really enjoy the design of vortrane site. Specially, we enjoy the strong iconic images they use, the way the tabs at the top scroll easily, and contact us page that generates an email. Lastly, I've included some photos of the concept we have been working on. What we are trying to demonstrate is how our company offers a range of services that are essentially linked together. We provide individual services that when combined present the full service package. We would like this concept to be integrated into the over concept of our website. Please feel free to ask for clarification of any of the above points or contact us if you have any additional questions. We appreciate all of your hard work and are very excited to see the updated designs. Best, Miriam Dowbrook Plenvaro Senior Program Manager miriam.dowbrook@plenvaro-mail.com

Industry/Entity Type

Government

Font styles to use
Serif
Sans Serif

Requirements
Must have
• Must work on/adapt to various/mobile devices (responsive)
Must be simple and straightforward
Colors should be in line/matching with logo
2 language versions: English and Arabic (no Thai)
Services should be the first group/row of items after/below the main image
Note: the website will be hosted by hostpeak
Nice to have
• Submit feedback form
What's New section
The banner at the bottom of the site should not be too large; we would like a narrow one more
It would be nice if the header/top banner (with Home, About, etc. tabs) could stay in place as you scroll down (like Vortrane and Chatterly)
We will likely only use one image with a Company slogan on the Home page rather than a carousel of images to rotate through
Should not have
• This is the existing website: http://www.plenvaro-example.org
We do not like the animation, the way the banner icons/titles bounce
Not simple enough, we don't like the functionality or how pages load so slowly
We do not like the logo centered - it should be at the left
The banner and its tabs should not be towards the right, we would like them to be centered, to go all the way across and to be below the logo

```html
<!DOCTYPE html>
<html lang="en">
<head>
<meta charset="utf-8">
<title>Plenvaro – Systems and Technology Consultants</title>
<link rel="stylesheet" href="https://fonts.googleapis.com/css2?family=Roboto:wght@300;400;500;700&display=swap">
<style>
:root{
  --red:#e3202a;
  --ink:#444;
  --muted:#7b7b7b;
  --page:#f5f5f5;
  --band:#ebebeb;
  --rule:#c9c9c9;
  --card:#f6f6f6;
  --footer:#555;
  --white:#fff;
}
*{box-sizing:border-box;margin:0;padding:0}
html,body{width:960px;height:1200px;overflow:hidden}
body{position:relative;background:var(--page);font-family:'Roboto',Arial,sans-serif;color:var(--ink)}
.abs{position:absolute}

/* header */
.site-header{position:absolute;left:0;top:0;width:960px;height:102px;background:var(--page);border-bottom:1px solid #ddd}
.brand{position:absolute;left:133px;top:38px;display:flex;align-items:center;gap:8px}
.brand-mark{width:18px;height:18px;background:var(--red)}
.brand-name{font-size:19px;font-weight:500;letter-spacing:3px;color:var(--red)}
.main-nav a{position:absolute;top:44px;font-size:10px;color:#555;text-decoration:none;line-height:15px}
.main-nav a.current{background:var(--red);color:var(--white);border-radius:3px;padding:1px 6px;top:42px;height:18px;line-height:16px}
.search-btn{position:absolute;left:810px;top:42px;width:17px;height:17px;border-radius:3px;background:var(--red)}

/* hero */
.hero{position:absolute;left:0;top:102px;width:960px;height:296px;
  background:radial-gradient(ellipse at 45% 35%,#a11a1e 0%,#5a1a1a 35%,#2a2222 65%,#141414 100%)}
.hero-title{position:absolute;left:134px;top:38px;font-size:37px;font-weight:500;color:var(--white)}
.service-list{position:absolute;left:134px;top:116px;list-style:none}
.service-list li{display:flex;align-items:center;gap:8px;font-size:14px;font-weight:300;color:var(--white);height:22.2px}
.hero-arrow{position:absolute;top:131px;width:36px;height:36px;background:rgba(30,30,30,.75)}
.hero-arrow.prev{left:8px}.hero-arrow.next{left:916px}

/* news */
.news{position:absolute;left:0;top:398px;width:960px;height:369px;background:linear-gradient(#ececec,#e7e7e7);border-bottom:1px solid #d4d4d4}
.section-head{position:absolute;height:16px;border-bottom:2px solid var(--rule);padding-bottom:18px}
.section-head h2{position:absolute;left:0;top:0;font-size:14px;font-weight:500;color:var(--ink)}
.section-head .view-all{position:absolute;right:0;top:2px;font-size:10px;color:var(--muted)}
.news-card{position:absolute;top:86px;width:163px;height:236px;background:var(--card);border:1px solid #d2d2d2}
.news-card .photo{height:88px;background:linear-gradient(135deg,#d9d9d9,#9a9a9a)}
.news-card h3{position:absolute;left:8px;top:100px;font-size:13px;font-weight:500;color:var(--ink)}
.news-card p{position:absolute;left:8px;top:130px;width:150px;font-size:10px;line-height:13.4px;color:var(--muted)}
.news-card .more{position:absolute;left:8px;top:211px;font-size:10px;font-weight:500;color:var(--red)}

/* events */
.event{position:absolute;left:134px;width:340px;height:52px}
.event .date{position:absolute;left:0;top:0;width:44px;height:51px;background:#e6e6e6;text-align:center;color:var(--muted);font-size:10px;line-height:12px;padding-top:5px}
.event .date b{display:block;font-size:13px;font-weight:500;color:var(--ink);line-height:16px}
.event h3{position:absolute;left:58px;top:0;font-size:13px;font-weight:500;color:var(--ink)}
.event p{position:absolute;left:58px;top:22px;width:290px;font-size:10px;line-height:15px;color:var(--muted)}

/* testimonial */
.quote{position:absolute;left:487px;top:853px;width:340px;height:117px;background:#e8e8e8;padding:7px 9px;font-size:10px;line-height:14.7px;color:var(--muted)}
.quote:after{content:"";position:absolute;left:47px;bottom:-10px;border:10px solid transparent;border-top-color:#e8e8e8;border-bottom:0}
.client-photo{position:absolute;left:516px;top:996px;width:54px;height:54px;background:linear-gradient(#bdbdbd,#555)}
.client-name{position:absolute;left:584px;top:1016px;font-size:10px;color:var(--muted)}
.client-name b{color:var(--ink);font-weight:500}
.slider-btn{position:absolute;top:812px;width:13px;height:13px;border-radius:3px;background:#bdbdbd}

/* footer */
.site-footer{position:absolute;left:0;top:1094px;width:960px;height:106px;background:var(--footer)}
.site-footer small{position:absolute;left:133px;top:46px;font-size:10px;color:var(--white)}
.social{position:absolute;top:43px;width:18px;height:18px;border-radius:50%;background:var(--white)}
</style>
</head>
<body>

<header class="site-header">
  <div class="brand"><span class="brand-mark"></span><span class="brand-name">PLENVARO</span></div>
  <nav class="main-nav">
    <a class="current" href="#" style="left:330px">HOME</a>
    <a href="#" style="left:394px">BUSINESS UNIT</a>
    <a href="#" style="left:498px">SERVICES</a>
    <a href="#" style="left:570px">ABOUT US</a>
    <a href="#" style="left:646px">LOCATIONS</a>
    <a href="#" style="left:726px">CONTACT US</a>
  </nav>
  <div class="search-btn">
    <svg width="17" height="17" viewBox="0 0 17 17"><circle cx="7.5" cy="7.5" r="3.5" fill="none" stroke="#fff" stroke-width="1.6"/><line x1="10" y1="10" x2="13" y2="13" stroke="#fff" stroke-width="2"/></svg>
  </div>
</header>

<section class="hero" role="img" aria-label="Blurred photo of red network cables plugged into a server switch">
  <h1 class="hero-title">Services we provide</h1>
  <ul class="service-list">
    <li><svg width="13" height="11" viewBox="0 0 13 11"><path d="M1 6l4 3.5L12 1.5" fill="none" stroke="#fff" stroke-width="2.4"/></svg>Consulting</li>
    <li><svg width="13" height="11" viewBox="0 0 13 11"><path d="M1 6l4 3.5L12 1.5" fill="none" stroke="#fff" stroke-width="2.4"/></svg>Engineering</li>
    <li><svg width="13" height="11" viewBox="0 0 13 11"><path d="M1 6l4 3.5L12 1.5" fill="none" stroke="#fff" stroke-width="2.4"/></svg>Construction</li>
    <li><svg width="13" height="11" viewBox="0 0 13 11"><path d="M1 6l4 3.5L12 1.5" fill="none" stroke="#fff" stroke-width="2.4"/></svg>Operations</li>
    <li><svg width="13" height="11" viewBox="0 0 13 11"><path d="M1 6l4 3.5L12 1.5" fill="none" stroke="#fff" stroke-width="2.4"/></svg>Maintenance</li>
  </ul>
  <div class="hero-arrow prev"><svg width="36" height="36" viewBox="0 0 36 36"><path d="M22 9l-9 9 9 9" fill="none" stroke="#bbb" stroke-width="4"/></svg></div>
  <div class="hero-arrow next"><svg width="36" height="36" viewBox="0 0 36 36"><path d="M14 9l9 9-9 9" fill="none" stroke="#bbb" stroke-width="4"/></svg></div>
</section>

<section class="news">
  <div class="section-head" style="left:133px;top:42px;width:694px"><h2>Latest News</h2><span class="view-all">View all</span></div>

  <article class="news-card" style="left:134px">
    <div class="photo" role="img" aria-label="Portrait photo of a businessman in a suit"></div>
    <h3>Lorem Ipsum</h3>
    <p>Lorem ipsum dolor sit amet, consectetur adipisicing elit, sed do eiusmod tempor incidi-dunt ut labore et dolore magna aliqua.</p>
    <span class="more">Read more</span>
  </article>
  <article class="news-card" style="left:310px">
    <div class="photo" role="img" aria-label="Photo of a presenter speaking to a seated audience" style="background:linear-gradient(135deg,#e4e4dc,#a9a98a)"></div>
    <h3>Lorem Ipsum</h3>
    <p>Lorem ipsum dolor sit amet, consectetur adipisicing elit, sed do eiusmod tempor incidi-dunt ut labore et dolore magna aliqua.</p>
    <span class="more">Read more</span>
  </article>
  <article class="news-card" style="left:487px">
    <div class="photo" role="img" aria-label="Photo of colleagues talking at a meeting table" style="background:linear-gradient(135deg,#d8d2c8,#8f8a84)"></div>
    <h3>Lorem Ipsum</h3>
    <p>Lorem ipsum dolor sit amet, consectetur adipisicing elit, sed do eiusmod tempor incidi-dunt ut labore et dolore magna aliqua.</p>
    <span class="more">Read more</span>
  </article>
  <article class="news-card" style="left:664px">
    <div class="photo" role="img" aria-label="Photo of a business team applauding" style="background:linear-gradient(135deg,#5a4a44,#2a2424)"></div>
    <h3>Lorem Ipsum</h3>
    <p>Lorem ipsum dolor sit amet, consectetur adipisicing elit, sed do eiusmod tempor incidi-dunt ut labore et dolore magna aliqua.</p>
    <span class="more">Read more</span>
  </article>
</section>

<div class="section-head" style="left:133px;top:808px;width:341px"><h2>Event Updates</h2><span class="view-all">View all</span></div>
<div class="section-head" style="left:487px;top:808px;width:340px"><h2>What Clients Say</h2></div>
<div class="slider-btn" style="left:798px"><svg width="13" height="13" viewBox="0 0 13 13"><path d="M8 3L4.5 6.5 8 10" fill="none" stroke="#fff" stroke-width="1.8"/></svg></div>
<div class="slider-btn" style="left:813px"><svg width="13" height="13" viewBox="0 0 13 13"><path d="M5 3l3.5 3.5L5 10" fill="none" stroke="#fff" stroke-width="1.8"/></svg></div>

<article class="event" style="top:853px">
  <div class="date"><b>17</b>MAY<br>2014</div>
  <h3>Lorem Ipsum</h3>
  <p>Lorem ipsum dolor sit amet, consectetur adipiscing elit. Nulla vehicula feugiat blandit. Nulla facilisi. Nulla tellus nisi...</p>
</article>
<article class="event" style="top:926px">
  <div class="date"><b>04</b>MAY<br>2014</div>
  <h3>Lorem Ipsum</h3>
  <p>Lorem ipsum dolor sit amet, consectetur adipiscing elit. Nulla vehicula feugiat blandit. Nulla facilisi. Nulla tellus nisi...</p>
</article>
<article class="event" style="top:999px">
  <div class="date"><b>23</b>APRIL<br>2014</div>
  <h3>Lorem Ipsum</h3>
  <p>Lorem ipsum dolor sit amet, consectetur adipiscing elit. Nulla vehicula feugiat blandit. Nulla facilisi. Nulla tellus nisi...</p>
</article>

<blockquote class="quote">Fusce ele mentum, nulla vel pellentesque consequat, ante nulla hen-drerit arcu, ac tincidunt mauris lacus sed leo. vamus suscipit molestie vestibulum.Fusce elementum, nulla vel pellentesque consequat, ante nulla hendrerit arcu, ac tincidunt mauris lacus sed leo. vamus suscipit molestie vestibulum.Fusce elementum, nulla vel pellentesque conse-quat, ante nulla hendrerit arcu, ac tincidunt mauris lacus sed leo. vamus suscipit molestie vestibulum.</blockquote>
<div class="client-photo" role="img" aria-label="Portrait photo of the client"></div>
<p class="client-name"><b>Tomas Reyl</b> - CEO Plenvaro</p>

<footer class="site-footer">
  <small>Plenvaro © 2014, All Rights Reserved</small>
  <span class="social" style="left:758px"></span>
  <span class="social" style="left:784px"></span>
  <span class="social" style="left:809px"></span>
</footer>

</body>
</html>
```